Urgent Cardiac Consult Request

We need a one page (1/2 pg size) order form for Urgent Cardiac Consults so that Emergency depts and walk -in clinics can fill this out and send forms with patient to our office. The page needs to have clear information, easy to read and to fill out. Our logo and address at the top and on the back side a map showing our location. I am sending a version that I have but the doctors want something different in the way of layout.
They want less information on them. At top - options for exam s: Excercise Stress Echo; Echocardiogram; Holter/Loop recorder (3day / 14 day/ other __); Concsult. Pt info in middle . Bottom : Indication s 1) Chest Pain/SOB 2: Palpatations 3) Other_____ Eyecatching, larger logo, etc Thanks

```html
<!DOCTYPE html>
<html lang="en">
<head>
<meta charset="utf-8">
<title>Rapid Cardiac Assessment – Order Form</title>
<link href="https://fonts.googleapis.com/css2?family=Roboto:ital,wght@0,400;0,500;0,700;1,400&family=Oswald:wght@500&family=Roboto+Condensed:wght@700&family=Open+Sans:wght@400&display=swap" rel="stylesheet">
<style>
  :root{
    --stage:#1561a9;
    --navy:#0d3a6e;
    --navy-deep:#0a2f5c;
    --callout:#1f2466;
    --red:#a3151c;
    --paper:#f4f5f7;
    --bar:#e2e4e8;
    --ink:#1d2430;
    --rule:#5a6068;
  }
  *{box-sizing:border-box;margin:0;padding:0}
  html,body{width:1200px;height:1101px;overflow:hidden}
  body{background:var(--stage);font-family:"Roboto",sans-serif;color:var(--ink);position:relative}

  .sheet{position:absolute;background:var(--paper);overflow:hidden}
  .sheet--map{left:136px;top:244px;width:446px;height:594px;background:#fff}
  .sheet--form{left:617px;top:244px;width:451px;height:591px}

  /* map side */
  .map-area{position:absolute;left:0;top:0;width:446px;height:474px;
    background:linear-gradient(165deg,#e4e5e8 0%,#dfe0e4 55%,#d9e6d8 100%)}
  .map-pin{position:absolute;left:202px;top:300px}
  .map-callout{position:absolute;left:230px;top:294px;width:119px;height:31px;border-radius:5px;
    background:var(--callout);color:#fff;font-family:"Open Sans",sans-serif;font-size:11px;line-height:12.5px;
    text-align:center;padding-top:3px}
  .clinic-block{position:absolute;left:22px;top:484px}
  .clinic-name{font-weight:700;font-size:14px;line-height:15px;letter-spacing:.6px;color:#111;text-transform:uppercase}
  .clinic-phone{font-family:"Roboto Condensed",sans-serif;font-weight:700;font-size:26px;line-height:26px;color:var(--red);letter-spacing:2px;margin-top:3px}
  .clinic-address{font-weight:700;font-size:12.5px;line-height:14px;color:#111}
  .brand-mark{position:absolute;left:340px;top:505px;display:flex;align-items:center;gap:6px;font-weight:700;font-size:11px;color:var(--navy)}
  .brand-mark .dot{width:22px;height:22px;border-radius:50%;background:var(--red)}
  .map-footer{position:absolute;left:0;bottom:0;width:100%;height:30px;background:var(--navy)}

  /* form side */
  .form-header{position:absolute;left:0;top:0}
  .form-title{position:absolute;left:28px;top:24px;font-family:"Oswald",sans-serif;font-weight:500;font-size:19px;color:#fff;letter-spacing:.3px}
  .logo-badge{position:absolute;left:252px;top:18px;width:156px;height:156px;border-radius:50%;background:#fff;border:3px solid var(--navy);display:flex;align-items:center;justify-content:center;text-align:center}
  .logo-badge span{font-weight:700;font-size:15px;line-height:17px;color:var(--navy);letter-spacing:.5px}
  .contact{position:absolute;left:29px;top:127px;font-size:11px;line-height:13px;font-weight:500}
  .contact .gap{margin-top:3px}

  .section-bar{position:absolute;height:16px;background:var(--bar);font-weight:700;font-size:11.5px;letter-spacing:.9px;line-height:16px;padding-left:12px;color:var(--navy)}
  .section-bar--red{color:var(--red)}
  .check{position:absolute;display:flex;align-items:center;gap:7px;font-size:11px;white-space:nowrap}
  .check::before{content:"";width:11px;height:11px;border:1.5px solid var(--navy);border-radius:2px;background:#fff}
  .check--small{font-size:9px;font-style:italic;gap:4px}
  .check--small::before{width:8px;height:8px;border-width:1.2px}
  .write-line{position:absolute;height:1px;background:var(--rule)}
  .field{position:absolute;display:flex;align-items:flex-end;gap:5px;font-size:10.5px;white-space:nowrap}
  .field::after{content:"";flex:1;height:1px;background:var(--rule);margin-bottom:3px}
  .field--plain::after{display:none}
  .field--plain{gap:14px}
  .field--plain .check{position:static}

  .form-footer{position:absolute;left:0;top:550px;width:100%;height:41px;background:var(--navy-deep);color:#fff;font-style:italic;font-size:8.4px;line-height:12px;text-align:center;padding-top:8px}
</style>
</head>
<body>

<section class="sheet sheet--map">
  <div class="map-area" role="img" aria-label="Street map of the surrounding neighbourhood with parks, main roads and a dashed approach route to the clinic"></div>
  <svg class="map-pin" width="16" height="22" viewBox="0 0 16 22" aria-hidden="true">
    <path d="M8 0C3.6 0 0 3.5 0 7.9 0 13.5 8 22 8 22s8-8.5 8-14.1C16 3.5 12.4 0 8 0z" fill="var(--red)"/>
    <circle cx="8" cy="8" r="3" fill="#fff"/>
  </svg>
  <div class="map-callout">180 Maple Ave<br>#4, Riverton</div>
  <div class="clinic-block">
    <p class="clinic-name">Lakeshore Heart Clinic &amp;<br>Diagnostic Centre</p>
    <p class="clinic-phone">555-010-4821</p>
    <p class="clinic-address">180 Maple Avenue Suite 4, Riverton</p>
  </div>
  <div class="brand-mark"><span class="dot"></span>Lakeshore<br>Heart</div>
  <div class="map-footer"></div>
</section>

<section class="sheet sheet--form">
  <svg class="form-header" width="451" height="200" viewBox="0 0 451 200" aria-hidden="true">
    <path d="M0 0H451V176Q410 110 330 80Q200 70 0 86Z" fill="var(--navy)"/>
    <path d="M0 90Q140 70 260 72L260 84Q140 82 0 108Z" fill="var(--red)"/>
  </svg>
  <h1 class="form-title">RAPID CARDIAC ASSESSMENT</h1>
  <div class="logo-badge"><span>LAKESHORE HEART<br>CLINIC</span></div>

  <div class="contact">
    <p>Phone : 555-010-4821</p>
    <p>Fax : 555-010-4830</p>
    <p class="gap">180 Maple Avenue, Suite 4, Riverton</p>
    <p>Monday - Saturday : 8am-5pm</p>
  </div>

  <div class="section-bar" style="left:28px;top:205px;width:395px">REQUEST FOR</div>
  <div class="check" style="left:41px;top:232px">Stress Echo/Test</div>
  <div class="check" style="left:179px;top:232px">EKG</div>
  <div class="check" style="left:276px;top:232px">Holter Monitor</div>
  <div class="check check--small" style="left:296px;top:249px">24-48 hrs</div>
  <div class="check check--small" style="left:355px;top:249px">7-14 days</div>
  <div class="check" style="left:41px;top:257px">Echocardiogram</div>
  <div class="check" style="left:41px;top:280px">Cardiology Consult If Positive</div>

  <div class="section-bar" style="left:28px;top:312px;width:395px">INDICATIONS</div>
  <div class="check" style="left:38px;top:344px">Chest Pain/SOB</div>
  <div class="check" style="left:144px;top:344px">Palpatations</div>
  <div class="check" style="left:232px;top:344px">Other</div>
  <div class="write-line" style="left:282px;top:352px;width:132px"></div>

  <div class="section-bar section-bar--red" style="left:28px;top:375px;width:190px">PATIENT INFORMATION</div>
  <div class="section-bar" style="left:234px;top:375px;width:189px">PHYSICIAN INFORMATION</div>

  <div class="field" style="left:29px;top:400px;width:189px">Name:</div>
  <div class="write-line" style="left:29px;top:436px;width:189px"></div>
  <div class="field" style="left:28px;top:447px;width:190px">Date of Birth:</div>
  <div class="field field--plain" style="left:28px;top:471px">Gender: <span class="check">Male</span><span class="check">Female</span></div>
  <div class="field" style="left:28px;top:495px;width:190px">Health Card#:</div>
  <div class="field" style="left:28px;top:517px;width:190px">Phone:</div>

  <div class="field" style="left:234px;top:400px;width:189px">Name:</div>
  <div class="field" style="left:234px;top:423px;width:189px">Billing #:</div>
  <div class="field" style="left:234px;top:448px;width:189px">Phone:</div>
  <div class="field" style="left:234px;top:472px;width:189px">Fax:</div>
  <div class="field" style="left:234px;top:496px;width:189px;font-size:9.6px;letter-spacing:-.2px">Ordering Physician Signature:</div>
  <div class="field" style="left:234px;top:519px;width:189px">Date:</div>

  <footer class="form-footer">
    PLEASE PROVIDE A COMPLETE LIST OF MEDICATIONS AT TIME OF TESTING AND/OR CONSULTATION.<br>
    ALL ABNORMAL RESULTS WILL BE FOLLOWED BY A CARDIOLOGY CONSULT UNLESS OTHERWISE NOTED
  </footer>
</section>

</body>
</html>
```